Business Card Design for Oncology Consulting Company

We need a business card design using a logo that has already been created.

Company name is: WMBHO - Guild for Tumor Projection, Therapy and Remediation

We would also like to include the following pieces of information on the business card:
Name
Title
US Address (street, city, state, zip, country)
Email address
Website address

Target Market(s)

The target customers are physicians (oncologists, pathologists) in Greece, Iran, US, etc who would refer patients to our company for a second medical opinion/genetic counseling for cancer.

Industry/Entity Type

Business

Colors

Designer to choose colors to be used in the design.

Requirements
Must have
• Must contain logo in attached file and elements described above.

```html
<!DOCTYPE html>
<html lang="en">
<head>
<meta charset="utf-8">
<title>WMBHO Business Card</title>
<link rel="stylesheet" href="https://fonts.googleapis.com/css2?family=Ubuntu:wght@400;500&display=swap">
<style>
  :root {
    --brand-blue: #2b6fb6;
    --ink-dark: #4a4f55;
    --card-white: #ffffff;
    --backdrop: #e4e6e8;
    --panel-text: #ffffff;
  }
  * { margin: 0; padding: 0; box-sizing: border-box; }
  html, body { width: 1200px; height: 898px; overflow: hidden; }
  body {
    background: var(--backdrop);
    font-family: "Ubuntu", Arial, sans-serif;
    position: relative;
  }
  .card {
    position: absolute;
    width: 540px;
    height: 309px;
    background: var(--card-white);
    box-shadow: 0 6px 18px rgba(0,0,0,0.18);
    overflow: hidden;
  }
  .card--back { left: 40px; top: 295px; }
  .card--front { left: 620px; top: 295px; }

  .company-name {
    position: absolute;
    color: var(--ink-dark);
    font-weight: 500;
    letter-spacing: 2px;
    line-height: 1;
    white-space: nowrap;
  }
  .card--back .company-name {
    left: 0; right: 0; top: 136px;
    text-align: center;
    font-size: 36px;
  }
  .card--front .company-name {
    left: 40px; top: 140px;
    font-size: 28px;
  }

  .edge-stripe {
    position: absolute;
    left: 0; top: 0;
    width: 6px; height: 100%;
    background: var(--brand-blue);
  }
  .contact-panel {
    position: absolute;
    right: 0; top: 0;
    width: 235px; height: 100%;
    background: var(--brand-blue);
    color: var(--panel-text);
    padding: 26px 20px 22px 14px;
    text-align: right;
    display: flex;
    flex-direction: column;
  }
  .contact-panel__name {
    font-size: 15px;
    font-weight: 500;
    letter-spacing: 2px;
    text-transform: uppercase;
  }
  .contact-panel__title {
    font-size: 10px;
    letter-spacing: 1.5px;
    text-transform: uppercase;
    margin-top: 3px;
  }
  .contact-panel__address {
    font-size: 12px;
    line-height: 1.45;
    margin-top: 30px;
    font-style: normal;
  }
  .contact-list {
    list-style: none;
    margin-top: 24px;
    font-size: 11px;
    line-height: 1;
  }
  .contact-list__item {
    display: flex;
    justify-content: flex-end;
    align-items: center;
    gap: 7px;
    margin-bottom: 9px;
  }
  .contact-list__icon { width: 11px; height: 11px; flex: none; }
</style>
</head>
<body>

<section class="card card--back" aria-label="Business card back">
  <span class="company-name">WMBHO</span>
</section>

<section class="card card--front" aria-label="Business card front">
  <div class="edge-stripe"></div>
  <span class="company-name">WMBHO</span>

  <div class="contact-panel">
    <h1 class="contact-panel__name">Daniel Hartley</h1>
    <p class="contact-panel__title">General Manager</p>
    <address class="contact-panel__address">418 Harlow Road,<br>Boston MA 02115 USA</address>
    <ul class="contact-list">
      <li class="contact-list__item">617 555 0148
        <svg class="contact-list__icon" viewBox="0 0 12 12"><path d="M2.5 1l2 2-1 1.3c.6 1.4 1.8 2.6 3.2 3.2l1.3-1 2 2-1.2 1.5C5 9.8 2.2 7 1 2.2z" fill="#fff"/></svg>
      </li>
      <li class="contact-list__item">617 555 0149
        <svg class="contact-list__icon" viewBox="0 0 12 12"><rect x="3" y="0.5" width="6" height="11" rx="1" fill="none" stroke="#fff"/><circle cx="6" cy="9.5" r="0.7" fill="#fff"/></svg>
      </li>
      <li class="contact-list__item">617 555 0150
        <svg class="contact-list__icon" viewBox="0 0 12 12"><rect x="1" y="5" width="10" height="6" fill="#fff"/><rect x="3" y="1" width="6" height="4" fill="none" stroke="#fff"/></svg>
      </li>
      <li class="contact-list__item">dhartley@wmbho.org
        <svg class="contact-list__icon" viewBox="0 0 12 12"><rect x="0.5" y="2.5" width="11" height="7" fill="#fff"/><path d="M0.5 2.5L6 7l5.5-4.5" fill="none" stroke="#2b6fb6"/></svg>
      </li>
      <li class="contact-list__item">www.wmbho-guild.org
        <svg class="contact-list__icon" viewBox="0 0 12 12"><circle cx="6" cy="6" r="5.3" fill="none" stroke="#fff"/><ellipse cx="6" cy="6" rx="2.3" ry="5.3" fill="none" stroke="#fff"/><path d="M0.7 6h10.6" stroke="#fff"/></svg>
      </li>
    </ul>
  </div>
</section>

</body>
</html>
```